Reminder card

We are an alternative health clinic. This project is for a postcard. The postcard is sent to our clients to remind them they have not been in the clinic for a long time and it's time for them to make an appointment. Our website is MeadowbrookWellness.com
Updates

Target Market(s)

Our clients are usually adults between the ages of 35 - 55, 70% women, 30% men. These are educated, wealthy, people who are committed to their health. Our clients expect us to be professional and an authority in our field, but friendly, playful and open.

Industry/Entity Type

Health

Font styles to use
Other font styles liked:
• our name is blackjack and the rest of the website is open sans

Requirements
Must have
• The front of the postcard must have our logo and name (see attached).

The front of the post card must have this text:
Feel good and want to stay that way? Need a boost? It's time for your tune-up appointment at Meadowbrook Wellness.

The right side on the back of the card must be blank for an address and stamp.

The left side on the back of the card must have our phone number (415.627.1943) and website (MeadowbrookWellness.com).
Nice to have
• We have an egg theme in our office. Our website is MeadowbrookWellness.com and if you look at it, you'll see the pictures of them.

The postcard should be in the same style as the website in color and tone.
Should not have
• We want things to be playful, but not look like something for children.

```html
<!DOCTYPE html>
<html lang="en">
<head>
<meta charset="utf-8">
<title>Meadowbrook Wellness – Reminder Postcard</title>
<link rel="stylesheet" href="https://fonts.googleapis.com/css2?family=Dancing+Script:wght@500&family=Open+Sans:wght@400&display=swap">
<style>
  :root {
    --stripe-grey: #b8c5cc;
    --stripe-light: #ffffff;
    --sky-deep: #5fb4ee;
    --sky-mid: #a9dcf8;
    --sky-pale: #eef8fe;
    --card-white: #ffffff;
    --ink: #111111;
    --shadow: rgba(0, 0, 0, 0.75);
    --sprout-green: #b7dc8f;
    --shell-peach: #f2b98c;
  }
  * { margin: 0; padding: 0; box-sizing: border-box; }
  html, body { width: 1200px; height: 1000px; overflow: hidden; }
  body {
    position: relative;
    background: repeating-linear-gradient(90deg,
      var(--stripe-light) 0 10px,
      var(--stripe-grey) 10px 30px);
    font-family: "Open Sans", Arial, sans-serif;
    color: var(--ink);
  }
  .postcard {
    position: absolute;
    left: 100px;
    width: 1000px;
    box-shadow: 5px 5px 6px var(--shadow);
    overflow: hidden;
  }
  .postcard--front { top: 25px; height: 443px; }
  .postcard--back { top: 530px; height: 438px; background: var(--card-white); }

  .sky-backdrop {
    position: absolute; inset: 0;
    background:
      radial-gradient(ellipse 45% 60% at 62% 30%, var(--sky-pale) 0%, rgba(238,248,254,0) 70%),
      radial-gradient(ellipse 40% 40% at 95% 95%, #ffffff 0%, rgba(255,255,255,0) 60%),
      linear-gradient(120deg, var(--sky-deep) 0%, var(--sky-mid) 35%, var(--sky-pale) 55%, var(--sky-mid) 75%, var(--sky-deep) 100%);
  }
  .brand-name {
    position: absolute; left: 52px; top: 38px;
    font-family: "Dancing Script", cursive;
    font-weight: 500;
    font-size: 44px;
    line-height: 1;
  }
  .seedling-photo {
    position: absolute;
    border-radius: 6px;
    background: linear-gradient(180deg, var(--sprout-green) 0%, var(--sprout-green) 35%, var(--shell-peach) 65%, var(--shell-peach) 100%);
  }
  .seedling-photo--front { left: 408px; top: 165px; width: 82px; height: 128px; }
  .seedling-photo--back { left: 20px; top: 18px; width: 92px; height: 136px; }

  .reminder-copy {
    position: absolute; left: 0; right: 0; top: 326px;
    text-align: center;
    font-size: 21px;
    line-height: 32.5px;
  }
  .contact-phone, .contact-web {
    position: absolute;
    font-family: "Dancing Script", cursive;
    font-weight: 500;
    white-space: nowrap;
  }
  .contact-phone { left: 118px; top: 121px; font-size: 21px; display: flex; align-items: center; gap: 2px; }
  .contact-phone svg { width: 16px; height: 20px; }
  .contact-web { left: 83px; top: 160px; font-size: 19px; }
</style>
</head>
<body>
  <section class="postcard postcard--front">
    <div class="sky-backdrop" role="img" aria-label="Bright blue sky with soft white light rays and clouds"></div>
    <h1 class="brand-name">Meadowbrook Wellness</h1>
    <div class="seedling-photo seedling-photo--front" role="img" aria-label="Photo of a green seedling growing from a cracked eggshell"></div>
    <p class="reminder-copy">
      Feel good and want to stay that way ?<br>
      Need a boost ?<br>
      It's time for your tune-up appointment at Meadowbrook Wellness.
    </p>
  </section>

  <section class="postcard postcard--back">
    <div class="seedling-photo seedling-photo--back" role="img" aria-label="Photo of a green seedling growing from a cracked eggshell"></div>
    <p class="contact-phone">
      <svg viewBox="0 0 16 20" aria-hidden="true">
        <path d="M4 1 L7 5 L5 7 Q6 11 9 14 L11 12 L14 15 L12 18 Q6 17 3 11 Q1 6 4 1 Z" fill="#111"/>
      </svg>
      415 627 1943
    </p>
    <p class="contact-web">www.meadowbrookwellness.com</p>
  </section>
</body>
</html>
```